Website front end design for an education nonprofit

This project involves design and development of the website front end (i.e., Web user interface and user experience design) for PAVO Tides, a nonprofit initiative for developing an online platform for basic English language instruction, especially targeted toward underprivileged, non-native English speaking populations.

More about us: We are a team of educators, researchers and engineers passionate about this cause and would like to invite talented, creative web developers to join us in this effort to create positive social impact! Please send a personal message to the project owner for the executive summary to get more information about our initiative, big picture vision and the team.

PAVO Tides website front end (UI/UX) design
Our key goals for this project are to develop an impressive Drupal-based front end for our website as well as to find really talented and creative web/UI/UX designers-cum-developers who are experts in the state-of-the-art web technologies, and are passionate about the cause of global online basic education. At the end of this project, we hope to have long term engagement with the selected developer(s) for our future website design and development needs.

Here are some preliminary guidelines on the PAVO Tides website front end framework as envisioned by us so far. Please note that we would very much encourage creative ideas and mock-ups from the developers.

1. Current platform: Our website prototype back-end uses Drupal CMS (we plan to continue using Drupal CMS) and at the moment, a toy front-end is based on the Drupal Skeleton platform for its simplicity, clean UI and mobile device friendliness. The web developer / designer can choose any Drupal front end as a starting point or come up with a new Drupal template that meets our requirements below. Prior experience and expertise on Drupal would be great.

2. Audience profile: While the primary audience for the website is expected to be young kids (6-10 years) not very familiar with English, the secondary audience also includes adults interested in basic English language skills. So the overall goal is to have simple, uncluttered / clean, elegant and lightweight (think loading time as well as mobile device friendliness) interface that is extremely intuitive and easy to navigate, is artistic and aesthetically appealing to a wide audience (especially the non-native English speaking populations). The most important point is that our target audience should feel welcome with the clean, crisp look and easy, user-centric navigation, and should in no case feel overwhelmed (say with too much text or clutter on the front page).

3. Front page: Here is a currently envisioned preliminary sketch of the website front page (very much open for refinement and improvements)
a. The top “menu bar” part of the landing page will have our organization name and logo along with (or above) the top menu bar with the following links and sub-links
i. “Learn” link with sub-menu of all our content sections (World learning, Basic sentence learning, Classic short stories, Picture Dictionary)
ii. “About” links with information about us (sub-menu entries: About PAVO Tides, Team, Supporters, Contributors)
iii. “Contribute” link with sub-menu entries Donate, Volunteer
iv. Menu entries towards the right side: “Login / sign up” followed by
v. “Search” with space to enter the search phrase
b. The middle “main page content” part of the page is where we would have entry points to our main content categories. The portion is envisioned to be graphical, with big blocks (images) as links to our content categories. The current categories (to start with) include 1. Word learning, 2. Basic sentence learning, and 3. Classic stories. We welcome creative ideas to represent these content categories in an appealing and elegant way (for example, these content categories could be portrayed as closed double doors that lead to the pages with the content. We would like to have placeholders for appropriate image links to different content categories – we should be able to put appropriate images or change them as we come up with new ideas that would work best with our target audience). The categories would change and grow as our content evolves, hence the core idea is to build a flexible framework that readily allows for expansion as well as customization.
c. The bottom menu / links bar portion of the landing page will have a list of links that are not included at the top. Examples include (with flexibility needed to add more when needed)
i. “Help”: this leads to a new page with FAQ, How to use
ii. “Contact us” link to a web contact form page
iii. “For Teachers” link to a page with information such as how to use, tips, pilot programs,
iv. “Volunteer” link to page with links such as Donate, Volunteer
v. “Contributors” that would link to a page with information about our Artists, Teachers, Writers, Developers etc.
vi. “Jobs” would link to a jobs page
vii. “Blog” would lead to our blog page
viii. “User stories” link to pages with feedback that we obtain from the users about how the content has helped them,
ix. Web 2.0 placeholders for social media (to be added later)

d. The footer of the website should include text “2013 PAVO Tides, All rights reserved.”

4. The middle block of the front page is the largest in screen real estate and perhaps the most challenging part that requires much creativity and thought on the UI/UX design aspect – the content pages pointed to by the section links on the middle portion of the front page are also being designed.

5. Color preference is towards soft, elegant (think grays, whites, light blues, other light colors) web safe colors. No harsh (too bright, garish) colors.

6. Fonts preference Nice, clean looking fonts (Arial alright) compatible across browsers.

7. Portability and robustness of the front page layout for different platforms should be carefully considered. Although our first launch target platform is PC (where cross browser compatibility is important), this would very soon be followed by mobile devices such as tablets and smartphones given their prevalence across the globe. This mobile friendly design or easy portability to mobile platforms with little work requirement should be considered as a design requirement.

8. Front page as a framework for the complete website: Note that the top and the bottom portions of the front page are envisioned be used as a common template / frame across all the pages of our website – the middle portion would be used to show our content on the other pages of our website.

9. UX: For the UI/UX design, it is critical to keep in mind key qualities such as ease of use, simplicity, elegance and artistic appeal. Some specific points to keep in mind: (1) the major portion of the target audience would be new to English and (2) young children are expected to be the primary audience but we want the website to appeal to adults interested in learning as well, and (3) we need the website to work even with relatively slow Internet speeds (for underdeveloped / developing regions especially), should always be kept in mind. HTML5 compliance ideas are encouraged.

10. Strictly not desired: Typical corporate feel seen in many webpages, blocky graphics, dull and uninviting overall look with no personality, Flash type effects, harsh colors.

11. Creativity and imagination necessary: We would like to reiterate that the designer/developer has complete freedom to re-imagine the front page considering the above requirements and get back with ideas for an inspiring layout that presents the content outlined above in an intuitive format, carefully considering our target audience.

A note: As a rule, we will always make sure that our developers and artists get proper credit for their work and are recognized and acknowledged by everyone visiting our website.

Expected deliverables:
Website design psd files AND coded webpage / Drupal template: the corresponding source code and all the required libraries, images etc would be required with minimal documentation / pointers on how to make changes and customizations.

Interested developers are encouraged to first send us preliminary prototype Design for the front page to get feedback on whether their approach and style is in line with our needs and preferences. We will suggest the developers to proceed further if the team thinks there is some potential for a match (of course, the final determination would be from the pool of shortlisted submissions) – otherwise, in case the team does not see potential for a match with our needs or if we have already received multiple submissions that are comparatively more closely aligned with our vision for the website, we'd prefer to be respectful of the developers’ time and effort by requesting them not to proceed further.

Please consider this effort as your contribution to an important social cause of global and accessible online education and not a commercial enterprise (our passion for making a positive impact is what is driving the PAVO Tides nonprofit team to undertake this initiative!). We would like to invite you to join us in this effort!

Reason: Due to requests from interested designers, we are extending the deadline. Looking forward to receiving many other creative designs!

Please see the project brief.

• Please see the project brief.

```html
<!DOCTYPE html>
<html lang="en">
<head>
<meta charset="utf-8">
<title>PAVO Tides – Learning Kids</title>
<link href="https://fonts.googleapis.com/css2?family=Arvo:wght@400;700&family=Signika:wght@300;400;600&display=swap" rel="stylesheet">
<style>
:root{
  --sky:#7fcccd;
  --footer:#a5e1ea;
  --deep:#0a6f94;
  --blue:#1688b8;
  --logo-bg:#1d6f8c;
  --white:#ffffff;
  --paper:#eef0f0;
  --btn-top:#8fe3f3;
  --btn-bottom:#2fb3d8;
  --field-line:#c9cfd1;
  --muted:#9aa4a8;
}
*{margin:0;padding:0;box-sizing:border-box}
html,body{width:1200px;height:904px;overflow:hidden}
body{background:var(--sky);font-family:"Signika",Arial,sans-serif;position:relative}
.abs{position:absolute}

/* header */
.brand{left:188px;top:-40px;width:282px;height:106px;border-radius:50%;background:var(--logo-bg)}
.brand-name{left:188px;top:8px;width:282px;text-align:center;font-family:"Arvo",serif;font-weight:700;font-size:21px;color:var(--white);letter-spacing:-0.5px}
.brand-tag{left:188px;top:31px;width:282px;text-align:center;font-family:"Arvo",serif;font-size:7.5px;color:var(--white);letter-spacing:.3px}
.account{top:11px;height:26px;border-radius:13px;background:linear-gradient(var(--btn-top),var(--btn-bottom));color:var(--deep);font-size:11px;text-align:center;line-height:26px;box-shadow:0 2px 3px rgba(0,0,0,.15)}
.social{top:44px;width:22px;height:22px;border-radius:50%}

/* nav */
.clouds{left:344px;top:78px;width:508px;height:96px;border-radius:48px;background:radial-gradient(ellipse at 50% 40%,#ffffff 55%,#e6f1f6 100%);box-shadow:0 6px 10px rgba(0,0,0,.12)}
.nav-item{top:118px;font-weight:600;font-size:14px;color:var(--blue);display:flex;align-items:center;gap:5px}
.chev{width:11px;height:11px}

/* hero */
.hero-kicker{left:196px;top:222px;font-family:"Arvo",serif;font-weight:700;font-size:17.5px;color:var(--white);text-shadow:0 0 1px var(--deep),1px 1px 0 rgba(10,111,148,.6);letter-spacing:-.2px}
.hero-title{left:198px;top:245px;font-family:"Arvo",serif;font-weight:700;font-size:56px;color:var(--white);text-shadow:2px 3px 3px rgba(0,0,0,.25);letter-spacing:-.5px}
.hero-sub{right:586px;top:296px;font-family:"Arvo",serif;font-size:27px;color:var(--blue)}
.hero-more{right:586px;top:336px;font-family:"Arvo",serif;font-size:15px;color:var(--blue)}
.hero-btn{left:464px;top:366px;width:154px;height:44px;border-radius:22px;background:linear-gradient(var(--btn-top),var(--btn-bottom));box-shadow:0 3px 5px rgba(0,0,0,.2);font-family:"Arvo",serif;font-size:20px;color:var(--deep);text-align:center;line-height:44px}
.hero-art{left:738px;top:188px;width:252px;height:236px;border-radius:46% 46% 20% 20%;background:radial-gradient(circle at 50% 45%,#6cc25a 0%,#b9cf4e 45%,#cf6a8a 75%,rgba(127,204,205,0) 100%)}
.ribbon{left:812px;top:394px;width:138px;height:34px;background:var(--white);clip-path:polygon(0 0,100% 0,92% 50%,100% 100%,0 100%)}
.ribbon-text{left:837px;top:398px;font-family:"Arvo",serif;font-size:19px;color:var(--blue)}
.badge{left:766px;top:380px;width:58px;height:58px;border-radius:50%;background:#7a7f1c;border:4px solid var(--white);box-shadow:0 2px 4px rgba(0,0,0,.25)}
.dot{top:439px;width:10px;height:10px;border-radius:50%;background:var(--white)}
.dot.active{background:var(--blue)}

/* signup strip */
.strip{left:195px;top:461px;width:797px;height:59px;background:linear-gradient(#f7f8f8,var(--paper));box-shadow:0 2px 3px rgba(0,0,0,.12)}
.field{top:478px;width:174px;height:26px;background:var(--white);border:1px solid var(--field-line);border-radius:2px;font-size:10px;color:var(--muted);line-height:24px;padding-left:15px;letter-spacing:.3px}
.submit{left:872px;top:479px;width:90px;height:26px;border-radius:13px;background:linear-gradient(var(--btn-top),var(--btn-bottom));font-family:"Arvo",serif;font-weight:700;font-size:11.5px;color:var(--deep);text-align:center;line-height:26px}
.plane{left:1012px;top:458px;width:50px;height:48px;border-radius:40%;background:linear-gradient(135deg,#e6c23a,#d86a2c)}

/* categories */
.cat-icon{top:580px;width:48px;height:48px;border-radius:4px}
.cat-title{top:586px;font-family:"Arvo",serif;font-weight:700;font-size:18px;line-height:20px;color:var(--blue)}
.cat-text{top:633px;width:210px;font-size:10px;line-height:11.5px;color:var(--white)}
.cat-more{top:681px;font-family:"Arvo",serif;font-size:9px;color:var(--deep);text-decoration:underline}
.divider{top:604px;height:80px;border-left:1px dashed var(--blue)}

/* footer */
.footer{left:0;top:744px;width:1200px;height:160px}
.foot-head{top:777px;font-family:"Arvo",serif;font-weight:700;font-size:14.5px;color:var(--blue);border-bottom:1px dotted var(--white);padding-bottom:2px}
.foot-list{top:798px;font-size:11.5px;line-height:16px;color:var(--white);list-style:none}
.foot-links{left:197px;top:875px;font-size:11.5px;color:var(--white)}
.copyright{right:202px;top:875px;font-size:11.5px;color:var(--white);letter-spacing:.3px}
</style>
</head>
<body>

<header>
  <div class="abs brand"></div>
  <div class="abs brand-name">PAVO TIDES</div>
  <div class="abs brand-tag">IOREM IPSUM DOLLAR EDUSA</div>

  <a class="abs account" style="left:856px;width:68px">LOGIN</a>
  <a class="abs account" style="left:928px;width:68px">SIGN UP</a>

  <div class="abs social" style="left:864px;background:#3b5a9a"></div>
  <div class="abs social" style="left:889px;background:#2aa5df"></div>
  <div class="abs social" style="left:914px;background:#136b96"></div>
  <div class="abs social" style="left:939px;background:#d0222c"></div>
  <div class="abs social" style="left:963px;background:#9a6a44"></div>

  <nav>
    <div class="abs clouds" role="img" aria-label="Fluffy white clouds behind the main menu"></div>
    <a class="abs nav-item" style="left:399px">HOME</a>
    <a class="abs nav-item" style="left:501px">LEARN
      <svg class="chev" viewBox="0 0 12 12"><circle cx="6" cy="6" r="6" fill="#1688b8"/><path d="M3.5 5 6 7.8 8.5 5" fill="none" stroke="#fff" stroke-width="1.6"/></svg></a>
    <a class="abs nav-item" style="left:626px">ABOUT
      <svg class="chev" viewBox="0 0 12 12"><circle cx="6" cy="6" r="6" fill="#1688b8"/><path d="M3.5 5 6 7.8 8.5 5" fill="none" stroke="#fff" stroke-width="1.6"/></svg></a>
    <a class="abs nav-item" style="left:723px">CONTRIBUTE
      <svg class="chev" viewBox="0 0 12 12"><circle cx="6" cy="6" r="6" fill="#1688b8"/><path d="M3.5 5 6 7.8 8.5 5" fill="none" stroke="#fff" stroke-width="1.6"/></svg></a>
  </nav>
</header>

<section class="hero">
  <div class="abs hero-kicker">RAISING THE LEARNING LEVELS OF STUDENTS IN HOME</div>
  <h1 class="abs hero-title">LEARNING KIDS</h1>
  <div class="abs hero-sub">raising the Knowledge</div>
  <div class="abs hero-more">TO LEARN MORE</div>
  <a class="abs hero-btn">SIGN UP</a>

  <div class="abs hero-art" role="img" aria-label="Illustration of a young girl reading a book in front of colourful rings"></div>
  <div class="abs ribbon"></div>
  <div class="abs ribbon-text">Learners</div>
  <div class="abs badge" role="img" aria-label="Green apple badge"></div>

  <div class="abs dot active" style="left:197px"></div>
  <div class="abs dot" style="left:210px"></div>
  <div class="abs dot" style="left:223px"></div>
  <div class="abs dot" style="left:236px"></div>
  <div class="abs dot" style="left:249px"></div>
</section>

<form class="signup">
  <div class="abs strip"></div>
  <svg class="abs" style="left:396px;top:488px" width="480" height="8">
    <path d="M0 4 Q20 7 42 3 M216 4 Q232 7 252 3 M426 4 Q446 7 476 3" fill="none" stroke="#a0a6a8" stroke-width="1.2" stroke-dasharray="5 3"/>
  </svg>
  <div class="abs field" style="left:222px">ENTER YOUR NAME</div>
  <div class="abs field" style="left:438px">YOUR EMAIL ADDERESS</div>
  <div class="abs field" style="left:648px">YOUR PHONE NUMBER</div>
  <a class="abs submit">SUBMIT</a>
  <svg class="abs" style="left:978px;top:470px" width="40" height="50">
    <path d="M2 2 L30 14 L2 48" fill="none" stroke="#ffffff" stroke-width="1.2"/>
  </svg>
  <div class="abs plane" role="img" aria-label="Toy paper plane pulling the sign-up banner"></div>
</form>

<section class="categories">
  <div class="abs cat-icon" style="left:197px;background:linear-gradient(#f4f4f4,#c8ccce)" role="img" aria-label="Word learning icon"></div>
  <h2 class="abs cat-title" style="left:252px">WORD<br>LEARNING</h2>
  <p class="abs cat-text" style="left:198px">Lorem ipsum dolor sit amet, consectetuer adipiscing elit, sed diam nonummy nibh euismod tincidunt ut laoreet dolore magna aliquam erat volutpat.</p>
  <a class="abs cat-more" style="left:199px">RAED MORE</a>

  <div class="abs divider" style="left:438px"></div>

  <div class="abs cat-icon" style="left:495px;background:linear-gradient(#3a7fe0,#1a4fb0)" role="img" aria-label="Basic sentence learning icon"></div>
  <h2 class="abs cat-title" style="left:548px;top:590px">BASIC SENTENCE<br>LEARNING,</h2>
  <p class="abs cat-text" style="left:496px;top:636px">Lorem ipsum dolor sit amet, consectetuer adipiscing elit, sed diam nonummy nibh euismod tincidunt ut laoreet dolore magna aliquam erat volutpat.</p>
  <a class="abs cat-more" style="left:497px;top:684px">RAED MORE</a>

  <div class="abs divider" style="left:752px"></div>

  <div class="abs cat-icon" style="left:792px;background:linear-gradient(#4a6fd0,#233c88)" role="img" aria-label="Classic stories book icon"></div>
  <h2 class="abs cat-title" style="left:846px;top:592px">CLASSIC<br>STORIES.</h2>
  <p class="abs cat-text" style="left:794px;top:636px">Lorem ipsum dolor sit amet, consectetuer adipiscing elit, sed diam nonummy nibh euismod tincidunt ut laoreet dolore magna aliquam erat volutpat.</p>
  <a class="abs cat-more" style="left:795px;top:684px">RAED MORE</a>
</section>

<footer>
  <svg class="abs footer" viewBox="0 0 1200 160" preserveAspectRatio="none">
    <path d="M0 6 L6 0 L12 6 L18 0 L24 6 L30 0 L36 6 L42 0 L48 6 L54 0 L60 6 L66 0 L72 6 L78 0 L84 6 L90 0 L96 6 L102 0 L108 6 L114 0 L120 6 L126 0 L132 6 L138 0 L144 6 L150 0 L156 6 L162 0 L168 6 L174 0 L180 6 L186 0 L192 6 L198 0 L204 6 L210 0 L216 6 L222 0 L228 6 L234 0 L240 6 L246 0 L252 6 L258 0 L264 6 L270 0 L276 6 L282 0 L288 6 L294 0 L300 6 L306 0 L312 6 L318 0 L324 6 L330 0 L336 6 L342 0 L348 6 L354 0 L360 6 L366 0 L372 6 L378 0 L384 6 L390 0 L396 6 L402 0 L408 6 L414 0 L420 6 L426 0 L432 6 L438 0 L444 6 L450 0 L456 6 L462 0 L468 6 L474 0 L480 6 L486 0 L492 6 L498 0 L504 6 L510 0 L516 6 L522 0 L528 6 L534 0 L540 6 L546 0 L552 6 L558 0 L564 6 L570 0 L576 6 L582 0 L588 6 L594 0 L600 6 L606 0 L612 6 L618 0 L624 6 L630 0 L636 6 L642 0 L648 6 L654 0 L660 6 L666 0 L672 6 L678 0 L684 6 L690 0 L696 6 L702 0 L708 6 L714 0 L720 6 L726 0 L732 6 L738 0 L744 6 L750 0 L756 6 L762 0 L768 6 L774 0 L780 6 L786 0 L792 6 L798 0 L804 6 L810 0 L816 6 L822 0 L828 6 L834 0 L840 6 L846 0 L852 6 L858 0 L864 6 L870 0 L876 6 L882 0 L888 6 L894 0 L900 6 L906 0 L912 6 L918 0 L924 6 L930 0 L936 6 L942 0 L948 6 L954 0 L960 6 L966 0 L972 6 L978 0 L984 6 L990 0 L996 6 L1002 0 L1008 6 L1014 0 L1020 6 L1026 0 L1032 6 L1038 0 L1044 6 L1050 0 L1056 6 L1062 0 L1068 6 L1074 0 L1080 6 L1086 0 L1092 6 L1098 0 L1104 6 L1110 0 L1116 6 L1122 0 L1128 6 L1134 0 L1140 6 L1146 0 L1152 6 L1158 0 L1164 6 L1170 0 L1176 6 L1182 0 L1188 6 L1194 0 L1200 6 L1200 160 L0 160 Z" fill="#a5e1ea"/>
  </svg>

  <h3 class="abs foot-head" style="left:195px">ABOUT US</h3>
  <p class="abs foot-list" style="left:195px;width:200px">Lorem ipsum dolor sit amet, consectetuer adipiscing elit, sed diam nonummy nibh euismod tincidunt ut laoreet dolore magna</p>

  <h3 class="abs foot-head" style="left:470px;width:130px">CONTRIBUTORS</h3>
  <ul class="abs foot-list" style="left:470px"><li>Artists,</li><li>Teachers,</li><li>Writers,</li><li>Developers</li></ul>

  <h3 class="abs foot-head" style="left:683px;width:108px">OTHER IINKS</h3>
  <ul class="abs foot-list" style="left:683px;top:799px"><li>Volunteer</li><li>Jobs</li><li>User Stories</li><li>Blog</li></ul>

  <h3 class="abs foot-head" style="left:872px;top:780px;width:116px">CONTACT US</h3>
  <address class="abs foot-list" style="left:872px;top:800px;font-style:normal">42 Maplebrook Lane<br>Suite 7<br>Harlow, NV 80210 US<br>04410 Valmora, Portugal</address>

  <div class="abs foot-links">Home | About Us | Patent Pending | Copy Right | Privacy | Contact Us Privacy</div>
  <div class="abs copyright">2013 PAVO TIDES, ALL RIGHTS RESERVED</div>
</footer>

</body>
</html>
```